Calm Fern Wellcare- Aged Care and Community Services

Looking for brochure to advertise our services. I will attach a draft that we do not want to use. Looking for graphics that are as natural as possible to present a personalised service. We supply services to aged people and people with disability. Please make it look classy and professional at the same time. I am looking for creativity. I have also attached the logo. Site addresses can be the last page. ideally looking for 2 designs, one A4 and another smaller possibly DL. Looking for creative out of the box thinkers. Thank you.

Target Market(s)

Aged Care service providers, disability service providers and private hospitals

Font styles to use
Serif
Sans Serif
Script

Colors
6b449b
886aae
eea4c8
f59195
fac994
3176b5
0555a3
cedeed
e4daeb

Requirements
Must have
• Targeted imagery, content and contact details
Nice to have
• personal profiles of people happy with our services

```html
<!DOCTYPE html>
<html lang="en">
<head>
<meta charset="utf-8">
<title>Calm Fern Wellcare – Brochure Spreads</title>
<link href="https://fonts.googleapis.com/css2?family=Montserrat:wght@400;500;700;800&family=Crimson+Text:ital,wght@0,400;1,400;1,700&family=Arimo:ital,wght@0,400;0,700;1,700&display=swap" rel="stylesheet">
<style>
  :root{
    --backdrop:#e9e9ec;
    --paper:#ffffff;
    --purple:#6b449b;
    --purple-deep:#5a2f8e;
    --magenta:#d0176f;
    --pink-soft:#f6d3e6;
    --lavender:#e4daeb;
    --navy:#2b2a6f;
    --ink:#3a3a46;
    --ink-soft:#5c5c68;
    --sky:#cedeed;
    --blue:#3176b5;
  }
  *{box-sizing:border-box;margin:0;padding:0}
  html,body{width:1200px;height:3000px;overflow:hidden}
  body{background:var(--backdrop);font-family:"Arimo",Arial,sans-serif;color:var(--ink);position:relative}
  .spread{position:absolute;left:40px;width:1120px;background:var(--paper);overflow:hidden;box-shadow:0 6px 24px rgba(0,0,0,.18)}
  .spread--cover{top:626px;height:828px}
  .spread--inner{top:1574px;height:800px}
  .abs{position:absolute}
  .band{position:absolute;left:0;top:0;width:1120px;height:100%}
  .photo{position:absolute}
  /* cover */
  .vision-mark{left:60px;top:40px;width:60px;height:60px;background:var(--magenta)}
  .vision-text{left:148px;top:42px;width:390px;font-size:15px;line-height:1.3;color:#2c2c36;font-weight:700;letter-spacing:.2px}
  .ghost-circle{left:90px;top:210px;width:300px;height:300px;border-radius:50%;background:radial-gradient(circle,#ececee 0%,#f4f4f6 60%,rgba(255,255,255,0) 72%)}
  .brand{font-family:"Montserrat",sans-serif;font-weight:700;color:var(--purple);text-align:center;line-height:1.1}
  .brand--left{left:170px;top:560px;width:230px;font-size:24px}
  .brand--right{left:700px;top:80px;width:300px;font-size:28px}
  .brand-dot{display:block;width:34px;height:34px;border-radius:50%;background:var(--purple);margin:0 auto 10px}
  .contact{color:#fff;font-size:12px;display:flex;align-items:center;gap:9px}
  .contact svg{flex:none}
  .contact--phone{left:60px;top:722px;font-family:"Montserrat",sans-serif;font-weight:700;font-size:15px}
  .contact--mail{left:62px;top:752px;font-size:10px}
  .contact--pin{left:330px;top:728px;font-size:10px}
  .contact--web{left:330px;top:754px;font-size:10px}
  .divider{left:312px;top:718px;width:1px;height:58px;background:rgba(255,255,255,.6)}
  .cover-title{left:596px;top:716px;font-family:"Montserrat",sans-serif;font-size:31px;color:#fff;letter-spacing:1px;font-weight:400}
  .cover-title b{font-weight:800}
  .cover-web{left:670px;top:784px;font-family:"Montserrat",sans-serif;font-size:11px;letter-spacing:4.5px;color:#fff;font-weight:700}
  .cover-web span{font-weight:400;opacity:.8}
  /* inner */
  .intro{left:57px;top:56px;width:262px;font-size:9.6px;line-height:1.3;color:var(--ink-soft);text-align:justify}
  .intro p{margin-bottom:10px}
  .intro strong{color:var(--magenta)}
  .quote{left:62px;top:430px;width:215px;padding-left:22px;border-left:5px solid var(--magenta);font-family:"Crimson Text",serif;font-style:italic;font-size:15px;line-height:1.25;color:#2a2a34}
  .quote em{color:var(--magenta)}
  .roles-lead{left:290px;top:428px;width:235px;font-size:10px;line-height:1.25;font-style:italic;font-weight:700;color:#2a2a34}
  .roles{left:318px;top:484px;list-style:none;font-size:9.6px;line-height:1.2;color:var(--ink)}
  .roles li{display:flex;align-items:flex-start;gap:12px;min-height:18px;margin-bottom:3px}
  .roles .num{flex:none;width:16px;height:16px;border-radius:50%;background:var(--navy);color:#fff;font-size:7.5px;display:flex;align-items:center;justify-content:center;font-weight:700}
  .roles .label{padding-top:2px}
  .round-photo{left:50px;top:556px;width:210px;height:210px;border-radius:50%;border:4px solid #fff;background:radial-gradient(circle at 45% 40%,#f4f7fb,#c9d8ea 70%,#aebfd6);box-shadow:0 0 0 1px #ddd}
  .section-head{font-family:"Montserrat",sans-serif;font-size:22px;color:var(--navy);font-weight:400;padding-left:14px;border-left:5px solid var(--magenta);line-height:1}
  .section-head b{font-weight:700}
  .head-believe{left:588px;top:62px}
  .head-partner{left:588px;top:235px}
  .belief{left:588px;top:100px;width:505px;font-family:"Crimson Text",serif;font-style:italic;font-size:18px;line-height:1.25;color:#2a2a34}
  .col-title{font-family:"Arimo",sans-serif;font-style:italic;font-weight:700;color:var(--magenta);font-size:14px}
  .col{width:235px;font-size:8.2px;line-height:1.3;color:var(--ink);text-align:justify}
  .col-1{left:588px;top:280px}
  .col-2{left:856px;top:280px}
  .col p{margin-top:8px}
  .inner-web{left:840px;top:768px;font-family:"Montserrat",sans-serif;font-size:10px;letter-spacing:3px;color:#fff}
  .gutter{left:559px;top:0;width:2px;height:100%;background:linear-gradient(90deg,rgba(0,0,0,.05),rgba(0,0,0,0))}
</style>
</head>
<body>

<section class="spread spread--cover" aria-label="Brochure cover spread">
  <div class="abs vision-mark"></div>
  <p class="abs vision-text">our vision is to be the most responsive staffing solutions provider in wa, whilst sourcing and placing staff that hold strong values which include ethics, accountability, respect, integrity and adapiability</p>
  <div class="abs ghost-circle"></div>

  <div class="photo" role="img" aria-label="Photo of three smiling medical staff, a doctor with a clipboard in the centre, with soft pink light rays behind"
       style="left:590px;top:200px;width:520px;height:520px;background:radial-gradient(ellipse at 55% 40%,#f7dbe9 0%,#f4e9f0 35%,#e8edf4 60%,#ffffff 85%)"></div>

  <svg class="band" viewBox="0 0 1120 828" aria-hidden="true">
    <defs>
      <linearGradient id="coverWash" x1="0" y1="0" x2="0" y2="1">
        <stop offset="0" stop-color="#fbe3ef" stop-opacity="0"/>
        <stop offset="1" stop-color="#fbe3ef" stop-opacity=".9"/>
      </linearGradient>
    </defs>
    <path d="M0,500 C200,620 420,690 560,690 L560,560 L0,470 Z" fill="url(#coverWash)"/>
    <path d="M0,530 C190,650 420,712 620,706 C820,700 1000,650 1120,605" fill="none" stroke="var(--magenta)" stroke-width="7"/>
    <path d="M0,560 C190,675 420,728 620,720 C820,712 1000,662 1120,618 L1120,828 L0,828 Z" fill="var(--purple)"/>
  </svg>

  <div class="abs brand brand--left"><span class="brand-dot"></span>Calm Fern Wellcare</div>
  <div class="abs brand brand--right">Calm Fern Wellcare</div>

  <div class="abs contact contact--phone">
    <svg width="16" height="16" viewBox="0 0 24 24"><path fill="#fff" d="M6.6 10.8a15.1 15.1 0 0 0 6.6 6.6l2.2-2.2c.3-.3.7-.4 1-.2 1.1.4 2.3.6 3.6.6.6 0 1 .4 1 1V20c0 .6-.4 1-1 1A17 17 0 0 1 3 4c0-.6.4-1 1-1h3.5c.6 0 1 .4 1 1 0 1.3.2 2.5.6 3.6.1.3 0 .7-.2 1z"/></svg>
    (03) 9555 0182
  </div>
  <div class="abs contact contact--mail">
    <svg width="12" height="12" viewBox="0 0 24 24"><rect x="2" y="5" width="20" height="14" rx="2" fill="none" stroke="#fff" stroke-width="2"/><path d="M2 7l10 7 10-7" fill="none" stroke="#fff" stroke-width="2"/></svg>
    admin@calmfernwellcare.example
  </div>
  <div class="abs divider"></div>
  <div class="abs contact contact--pin">
    <svg width="12" height="14" viewBox="0 0 24 28"><path fill="#fff" d="M12 0a9 9 0 0 0-9 9c0 7 9 17 9 17s9-10 9-17a9 9 0 0 0-9-9zm0 13a4 4 0 1 1 0-8 4 4 0 0 1 0 8z"/></svg>
    12 Example Lane Perth WA 6000 Australia
  </div>
  <div class="abs contact contact--web">
    <svg width="12" height="12" viewBox="0 0 24 24"><circle cx="12" cy="12" r="10" fill="none" stroke="#fff" stroke-width="2"/><path d="M2 12h20M12 2c3 3 3 17 0 20M12 2c-3 3-3 17 0 20" fill="none" stroke="#fff" stroke-width="1.6"/></svg>
    www.calmfernwellcare.example
  </div>

  <h1 class="abs cover-title">REMAGINING <b>HEALTHCARE</b></h1>
  <p class="abs cover-web">www.calmfernwellcare<span>.example</span></p>
  <div class="abs gutter"></div>
</section>

<section class="spread spread--inner" aria-label="Brochure inside spread">
  <div class="abs intro">
    <p><strong>Calm Fern Wellcare is a Perth based staffing solutions providers which thrives</strong> to partner with organisations in meeting their continuing resource requirements. We are slowly building a reputation on our responsiveness to client enquiries, whilst meeting our key service deliverables. We work with service providers in Residential Aged Care, Community Supports and Hospitals.</p>
    <p><strong>We believe in the key to building lasting relationships in life to have a willingness</strong> and ability to reciprocity which we aim to do by understanding the intricate needs of our clients, collaboratively identify problems, help them progress from their current situation, earn trust and thrive for excellence.</p>
    <p><strong>Our vision is to be the most responsive staffing solution provider in WA,</strong> whilst sourcing and placing staff that hold strong values which include ethics, accountability, respect, integrity and adaptable. Our mission is to partner with like-minded organisations that genuinely thrive in making a difference, are ethically placed in society, have effective governance at the care of their operations.</p>
  </div>
  <div class="photo" role="img" aria-label="Photo of a doctor reviewing an x-ray with an elderly woman in a bright clinic"
       style="left:330px;top:45px;width:230px;height:355px;background:linear-gradient(135deg,#eef4f9 0%,#d6e4f0 50%,#c3d3e6 100%)"></div>

  <p class="abs quote">our diverse database of skilled staff gives you the peace of mind you need to do what you do best, look after <em>your customers.</em></p>
  <p class="abs roles-lead">We actively source and recruit skills professionals with direct cultural fit to most of our clients. These roles include but are not limited to:</p>

  <svg class="band" viewBox="0 0 1120 800" aria-hidden="true">
    <path d="M0,655 C160,712 380,752 620,756 C830,760 1000,730 1120,690" fill="none" stroke="var(--magenta)" stroke-width="6"/>
    <path d="M0,676 C160,732 380,768 620,772 C830,776 1000,746 1120,706 L1120,800 L0,800 Z" fill="var(--purple)"/>
  </svg>

  <ul class="abs roles">
    <li><span class="num">01</span><span class="label">Registered Nurses</span></li>
    <li><span class="num">02</span><span class="label">Enrolled Nurses</span></li>
    <li><span class="num">03</span><span class="label">Nursing Assistants/Carers</span></li>
    <li><span class="num">04</span><span class="label">Allied Health Assistants<br>(Physiotherapy &amp; OT)</span></li>
    <li><span class="num">05</span><span class="label">Chefs and Cooks (healthcare<br>experienced)</span></li>
    <li><span class="num">06</span><span class="label">Catering Staff and Kitchen hands</span></li>
    <li><span class="num">07</span><span class="label">Cleaning and Domestic Assistants</span></li>
    <li><span class="num">08</span><span class="label">Laundry Attendant and</span></li>
    <li><span class="num">09</span><span class="label">*many more related professionals</span></li>
  </ul>

  <div class="abs round-photo" role="img" aria-label="Round photo of a smiling doctor holding the hand of an elderly patient"></div>

  <h2 class="abs section-head head-believe">Whate <b>we belive</b></h2>
  <p class="abs belief">A person who is appreciated, always does more than what is expected. Our staff are at the centre of all our decisions as we are only as good as the people we hire. If we look after our staff, they will look after our client.</p>
  <h2 class="abs section-head head-partner">Why <b>partner with us</b></h2>

  <div class="abs col col-1">
    <h3 class="col-title">SERVICE DESIGN</h3>
    <p>Prior to placing all staff, we ensure we have conducted a full client profile to understand your business needs, its end-to-end operations, service delivery, HR and governance. This will enable us to design a service around your specific needs which allows for a seamless integration. We encourage continuity of service delivery which we implement by ensuring the same staff are placed at your sites. Culturally, this enables our staff to build relationships with your teams and customers allowing for a natural fit.</p>
  </div>
  <div class="abs col col-2">
    <h3 class="col-title">TECHNOLOGY</h3>
    <p>We have integrated our systems with necessary technology as we believe technology is a part of modern day efficiencies. People are our business and nothing can replace human relationships, interactions or connection, however to effectively enhance these human related characteristics, technology helps us in maximising efficiencies and minimising error. Our on-boarding and scheduling platforms are automated, further solidifying compliance and managing risk.</p>
  </div>

  <div class="photo" role="img" aria-label="Photo of two laboratory workers in protective suits reviewing results"
       style="left:590px;top:432px;width:530px;height:300px;background:linear-gradient(160deg,#e4eef8 0%,#bcd3ea 45%,#8fb3d9 100%)"></div>
  <svg class="band" viewBox="0 0 1120 800" aria-hidden="true" style="pointer-events:none">
    <path d="M560,752 C720,758 900,742 1120,700 L1120,800 L560,800 Z" fill="var(--purple)"/>
    <path d="M560,748 C720,754 900,736 1120,694" fill="none" stroke="var(--magenta)" stroke-width="5"/>
  </svg>
  <p class="abs inner-web">www.calmfernwellcare.example</p>
  <div class="abs gutter"></div>
</section>

</body>
</html>
```